Book cover for a sci fi book called The Velvet Assembly

Dear Pixel Harbor team,

I would need a book cover design for my sci fi book, 'The Velvet Assembly'.

I will start by briefing you about the book's content, then I would like to advice you about a few possible book cover scenarios that I could imagine having for the book, and on which I would like to ask you to work on.

Book abstract:

The velvet assembly is a technically developed and spiritually evolved society from a distant galaxy.

Main location the actions take place: Planet Earth, globalized world, former Northern Germany, a new isolated high tech city at the sea, called Lees, inhabitants from everywhere, one government, one religion.
• Year: 2093
• The Velvet Assembly: solar system with 7 suns. The inhabitans of the velvet assembly have no physical body, only energetical bodies. Only when visiting Earth, they can incarnate at will.

The action starts on planet Earth, where a group of 4 people, two women and two males, who meet through different circumstances and decide to follow together a spiritual and philiosophical path towards self development and evolution. They meet an incarnated master from the velvet assembly who leads their path. At the end of the books, they reach a form of enlightment and transcende to The Velvet Assembly, they only come to know at the end the truth about the real origin of their master.

For the book cover, no matter what ideas you choose, please use max three predominant colors for that, red, yellow and orange. The book cover should inspire warmth.

Suggestions for the design:
- an abstract sun
- a cosmic view of the velvet assembly
- an abstractized design of a sacred geometry shape
- sun in the upper left corner, shining with visible rays on the whole surface of the book cover, a group of 4 people with the female old master sitting by their side in the lower right corner
- an out of the box Ufo, please choose for example an asymmetrical shape, definately not the usual flying sorcer, departing from the velvet assembly solar system, cosmic view from above
- PLEASE FEEL FREE TO BRAINSTROM ON YOUR OWN IDEAS BASED ON WHAT THE BOOK ABSTRACT INSPIRED YOU

For any questions, I am atbyour disposal.

I am looking forward to your design, thank you in advance for that.

Kind regards,
Mira

Target Market(s)

Sci Fi enthusiasts
Philosophers

Font styles to use
Serif

Colors
fbee3e
ffc214
faa54b
f37122
f04a50

Requirements
Must have
• For the book cover, no matter what ideas you choose, please use max three predominant colors for that, red, yellow and orange and/or any derived hues. The book cover should inspire warmth.
• Suggestions for the design:
• - an abstract sun
• - a cosmic view of the velvet assembly
• - an abstractized design of a sacred geometry shape
• - sun in the upper left corner, shining with visible rays on the whole surface of the book cover, a group of 4 people with the female old master sitting by their side in the lower right corner
• - an out of the box Ufo, please choose for example an asymmetrical shape, definately not the usual flying sorcer, departing from the velvet assembly solar system, cosmic view from above
• - PLEASE FEEL FREE TO BRAINSTROM ON YOUR OWN IDEAS BASED ON WHAT THE BOOK ABSTRACT INSPIRED YOU
Nice to have
• Minimalistic and modern design
Should not have
• dark or grey shades
• phtographs

```html
<!DOCTYPE html>
<html lang="en">
<head>
<meta charset="utf-8">
<title>The Velvet Assembly — Book Cover</title>
<link rel="stylesheet" href="https://fonts.googleapis.com/css2?family=Cinzel:wght@400;500&family=EB+Garamond&display=swap">
<style>
  :root {
    --ink-red: #e0301e;
    --spine-red: #e8361a;
    --spine-orange: #f46a1c;
    --sun-yellow: #fbee3e;
    --sun-gold: #ffc214;
    --sun-orange: #f37122;
    --paper: #ffffff;
  }
  * { margin: 0; padding: 0; box-sizing: border-box; }
  html, body { width: 1200px; height: 830px; overflow: hidden; background: var(--paper); }
  .cover-wrap { position: relative; width: 1200px; height: 830px; background: var(--paper); }

  .title { font-family: "Cinzel", serif; color: var(--ink-red); text-align: center; line-height: 1; font-weight: 400; }
  .title .line-small { display: block; font-size: 52px; letter-spacing: 1px; }
  .title .line-big { display: block; font-size: 92px; letter-spacing: 0; }
  .title .cap { font-size: 1.18em; }

  .back-cover { position: absolute; left: 0; top: 0; width: 554px; height: 830px; }
  .back-cover .title { position: absolute; left: 20px; width: 514px; top: 44px; }
  .back-cover .title .line-small { font-size: 44px; }
  .back-cover .title .line-big { font-size: 78px; margin-top: -2px; }
  .blurb { position: absolute; left: 42px; top: 196px; width: 467px; font-family: "EB Garamond", serif; font-size: 14.2px; line-height: 18.4px; color: var(--ink-red); text-align: justify; hyphens: auto; }
  .blurb p + p { margin-top: 18px; }

  .spine { position: absolute; left: 554px; top: 0; width: 92px; height: 830px;
    background: radial-gradient(ellipse at 40% 30%, var(--spine-orange), var(--spine-red) 70%); }
  .spine-text { position: absolute; left: 92px; top: 0; width: 830px; height: 92px; transform-origin: 0 0; transform: rotate(90deg); font-family: "Cinzel", serif; color: var(--paper); }
  .spine-title { position: absolute; left: 150px; top: 4px; line-height: 1; }
  .spine-title .line-small { display: block; font-size: 26px; }
  .spine-title .line-big { display: block; font-size: 48px; }
  .spine-author { position: absolute; left: 506px; top: 44px; font-size: 24px; letter-spacing: 10px; line-height: 1; }

  .front-cover { position: absolute; left: 646px; top: 0; width: 554px; height: 830px; }
  .front-cover .title { position: absolute; left: 0; width: 554px; top: 52px; }
  .front-cover .title .line-big { margin-top: -4px; }
  .cover-art { position: absolute; left: 48px; top: 244px; width: 468px; height: 468px; }
  .author { position: absolute; left: 0; width: 554px; top: 752px; text-align: center; font-family: "Cinzel", serif; color: var(--ink-red); font-size: 40px; letter-spacing: 14px; line-height: 1; padding-left: 14px; }
</style>
</head>
<body>
<div class="cover-wrap">

  <section class="back-cover">
    <h2 class="title">
      <span class="line-small"><span class="cap">T</span>HE <span class="cap">V</span>ELVET</span>
      <span class="line-big"><span class="cap">A</span>SSEMBLY</span>
    </h2>
    <div class="blurb">
      <p>Lorem ipsum dolor sit amet, consectetur adipiscing elit. Fusce iaculis, nunc non iaculis mollis, ante diam consequat ipsum, vitae commodo arcu ante et eros. Sed augue est, porta in mi a, mollis facilisis est. Pellentesque tincidunt, sem sed pellentesque egestas, diam tortor rhoncus eros, ut iaculis turpis velit non ex. Etiam orci odio, commodo sed ante eget, bibendum consequat risus. Vivamus ullamcorper, ante a sagittis lacinia, felis turpis efficitur felis, ut dapibus odio dui nec leo. Donec accumsan faucibus sapien, quis elementum dui porttitor quis. Etiam aliquam diam id quam feugiat porttitor. Fusce sodales quam a rhoncus pellentesque. Curabitur nibh massa, vestibulum in orci non, pretium bibendum metus. Nulla ut nibh pretium, ullamcorper sapien sed, malesuada ligula.</p>
      <p>Etiam dictum, tellus non laoreet vehicula, purus arcu mattis elit, at scelerisque purus tortor vel enim. Pellentesque tellus sapien, ullamcorper ut nibh vel, tincidunt tempor ante. Curabitur rhoncus porttitor sollicitudin. Vestibulum non neque libero. Pellentesque id elit nec nisi pellentesque dapibus. Proin pulvinar auctor ullamcorper. Nunc ut tempor mauris, quis pulvinar risus. Etiam dictum sit amet odio vel fermentum. Aliquam eu vestibulum urna. Aliquam feugiat pharetra mi, non sollicitudin dui egestas eget. Donec non orci finibus, hendrerit velit pretium, aliquam magna. Aliquam suscipit tellus augue, quis molestie odio cursus sit amet.</p>
    </div>
  </section>

  <section class="spine">
    <div class="spine-text">
      <div class="spine-title">
        <span class="line-small">THE VELVET</span>
        <span class="line-big">ASSEMBLY</span>
      </div>
      <div class="spine-author">AUTHOR NAME</div>
    </div>
  </section>

  <section class="front-cover">
    <h1 class="title">
      <span class="line-small"><span class="cap">T</span>HE <span class="cap">V</span>ELVET</span>
      <span class="line-big"><span class="cap">A</span>SSEMBLY</span>
    </h1>
    <svg class="cover-art" viewBox="0 0 468 468" role="img" aria-label="Illustration of a glowing yellow sun at the centre of a red cosmic disc with orbit rings and stars">
      <defs>
        <radialGradient id="sunDisc" cx="50%" cy="50%" r="50%">
          <stop offset="0" stop-color="var(--sun-yellow)"/>
          <stop offset="0.2" stop-color="var(--sun-gold)"/>
          <stop offset="0.38" stop-color="var(--sun-orange)"/>
          <stop offset="1" stop-color="var(--spine-red)"/>
        </radialGradient>
      </defs>
      <circle cx="234" cy="234" r="234" fill="url(#sunDisc)"/>
    </svg>
    <div class="author">AUTHOR NAME</div>
  </section>

</div>
</body>
</html>
```